Harbor Vault Works Business Card Design

I would like someone to design a business card that is similar to the top design on the safes in the pictures. I like the curvature of the wording on the safes and I like the font and the scrolling from the Meridian Western signs I sent. I would also like to incorporate king neptune/ posidon in the center of scroll above "Harbor Vault Works"

Target Market(s)

Gun Safes

Industry/Entity Type

Business

Contact Information for Business Card

The scrolling should be on the sides and throughout the "Harbor Vault Works" arching in the top of the card.

Font styles to use
Decorative

Colors

Designer to choose colors to be used in the design.

Requirements
Must have
• Scrolling, old school font
Nice to have
• some image of king neptune/ posidon in the scroll

```html
<!DOCTYPE html>
<html lang="en">
<head>
<meta charset="utf-8">
<title>Harbor Vault Works – Business Card</title>
<link rel="stylesheet" href="https://fonts.googleapis.com/css2?family=Source+Sans+3:wght@400;600&display=swap">
<style>
  :root {
    --backdrop: #000000;
    --card: #2f3034;
    --card-edge: #34353a;
    --ink: #f2f2f2;
    --ink-soft: #e4e4e4;
    --divider: rgba(255, 255, 255, 0.07);
  }
  * { margin: 0; padding: 0; box-sizing: border-box; }
  html, body {
    width: 1200px;
    height: 900px;
    overflow: hidden;
    background: var(--backdrop);
    font-family: "Source Sans 3", "Segoe UI", sans-serif;
    color: var(--ink);
  }
  .canvas { position: relative; width: 1200px; height: 900px; }
  .card {
    position: absolute;
    top: 271px;
    width: 456px;
    height: 281px;
    border-radius: 14px;
    background: linear-gradient(180deg, var(--card-edge), var(--card));
  }
  .card--front { left: 137px; }
  .card--back { left: 627px; }

  .brand-stack {
    position: absolute;
    font-weight: 600;
    text-transform: uppercase;
    color: var(--ink);
    line-height: 1.02;
  }
  .card--front .brand-stack {
    left: 62px;
    top: 96px;
    font-size: 22px;
    letter-spacing: 0.5px;
  }
  .card--back .brand-stack {
    left: 170px;
    top: 96px;
    font-size: 31px;
    letter-spacing: 1px;
  }
  .brand-dot {
    position: absolute;
    left: 120px;
    top: 124px;
    width: 34px;
    height: 34px;
    border-radius: 50%;
    background: var(--ink-soft);
  }

  .divider {
    position: absolute;
    left: 213px;
    top: 50px;
    width: 1px;
    height: 180px;
    background: var(--divider);
  }
  .contact-block { position: absolute; left: 249px; top: 62px; }
  .person-name { font-size: 19px; font-weight: 400; line-height: 1.2; }
  .person-role { font-size: 12.5px; line-height: 1.3; color: var(--ink-soft); }
  .address { margin-top: 11px; font-size: 13px; line-height: 16.5px; color: var(--ink-soft); }
  .contact-list { margin-top: 10px; list-style: none; font-size: 12.5px; line-height: 16.5px; color: var(--ink-soft); }
  .contact-list li { display: flex; align-items: center; gap: 6px; }
  .contact-list svg { width: 10px; height: 10px; fill: var(--ink-soft); flex: none; }
</style>
</head>
<body>
<div class="canvas">
  <section class="card card--front" aria-label="Business card front">
    <div class="brand-stack">Harbor<br>Vault<br>Works</div>
    <div class="divider"></div>
    <div class="contact-block">
      <p class="person-name">Daniel Reeve</p>
      <p class="person-role">Managing Director</p>
      <p class="address">12345, Address Goes Here<br>Country Name, 123456.</p>
      <ul class="contact-list">
        <li><svg viewBox="0 0 10 10"><path d="M2.2 0.6 3.6 2.6 2.8 3.6Q3.8 5.8 6.4 7.2L7.4 6.4 9.4 7.8 8.4 9.4Q4.6 9.2 1.6 5.6 0.4 3.6 0.6 1.6Z"/></svg>044-123 456 789</li>
        <li><svg viewBox="0 0 10 10"><path d="M0.5 2h9v6h-9z M0.5 2 5 5.4 9.5 2" fill="none" stroke="#e4e4e4" stroke-width="1"/><path d="M0.5 2h9L5 5.4z"/></svg>hello@harborvault.example</li>
        <li><svg viewBox="0 0 10 10"><path d="M4 6 6 4 M3.2 4.6 1.8 6a1.6 1.6 0 0 0 2.2 2.2L5.4 6.8 M6.8 5.4 8.2 4A1.6 1.6 0 0 0 6 1.8L4.6 3.2" fill="none" stroke="#e4e4e4" stroke-width="1.2" stroke-linecap="round"/></svg>www.harborvault.example</li>
      </ul>
    </div>
  </section>

  <section class="card card--back" aria-label="Business card back">
    <div class="brand-dot"></div>
    <div class="brand-stack">Harbor<br>Vault<br>Works</div>
  </section>
</div>
</body>
</html>
```